Residential Construction Business - Site Signage

I need a design made for a site fence banner. We have a logo and branding so the design would need to be aligned with this. It would need to be made to specific size ratio so that it can be sent to the maker for production.
ratio : 4600 wide x 1700 high
The design should feature our website and also the slogan
"don't move, re-imagine"

Target Market(s)

potential clients

Industry/Entity Type

construction

Font styles to use
Other font styles liked:
• to match branding

Colors
0054AA
0677BA
7BADD7
CADEEF
E8F1F8

Requirements
Must have
• www.velmbuild.com.au Majority of the sign is our brand logo
Nice to have
• Majority of the sign is our brand logo
Should not have
• colors and themes that arent brand relevant

```html
<!DOCTYPE html>
<html lang="en">
<head>
<meta charset="utf-8">
<title>Velm Build – Site Fence Banner</title>
<link rel="stylesheet" href="https://fonts.googleapis.com/css2?family=Antonio:wght@300;400&family=Montserrat:wght@500;600&display=swap">
<style>
  :root {
    --page-bg: #e4e4e4;
    --banner-white: #ffffff;
    --banner-charcoal: #3d3d3f;
    --brand-navy: #043a5a;
    --text-light: #ffffff;
  }
  html, body {
    margin: 0;
    padding: 0;
    width: 1200px;
    height: 600px;
    overflow: hidden;
    background: var(--page-bg);
  }
  .canvas {
    position: relative;
    width: 1200px;
    height: 600px;
    display: flex;
    align-items: center;
    justify-content: center;
  }
  .fence-banner {
    display: block;
    width: 1120px;
    height: 415px;
  }
  .banner-white { fill: var(--banner-white); }
  .banner-charcoal { fill: var(--banner-charcoal); }
  .divider { stroke: var(--text-light); stroke-width: 1.2; }
  .brand-square { fill: var(--brand-navy); }
  .brand-name {
    font-family: "Montserrat", sans-serif;
    font-weight: 600;
    font-size: 30px;
    letter-spacing: 6px;
    fill: var(--brand-navy);
  }
  .slogan {
    font-family: "Antonio", sans-serif;
    fill: var(--text-light);
  }
  .slogan-lead { font-weight: 300; font-size: 52px; }
  .slogan-main { font-weight: 400; font-size: 66px; }
  .website {
    font-family: "Montserrat", sans-serif;
    font-weight: 500;
    font-size: 15.5px;
    fill: var(--text-light);
  }
</style>
</head>
<body>
<main class="canvas">
  <svg class="fence-banner" viewBox="0 0 1080 400" xmlns="http://www.w3.org/2000/svg" aria-labelledby="banner-title">
    <title id="banner-title">Velm Build – don't move, re-imagine – www.velmbuild.com.au</title>

    <rect class="banner-white" x="0" y="0" width="1080" height="400"/>
    <path class="banner-charcoal" d="M545 0 H1080 V400 H528 L674 216 Q690 195 674 174 Z"/>

    <g class="brand-lockup">
      <rect class="brand-square" x="59" y="63" width="274" height="274"/>
      <text class="brand-name" x="356" y="212" textLength="290" lengthAdjust="spacing">VELM BUILD</text>
    </g>

    <line class="divider" x1="814" y1="0" x2="814" y2="60"/>

    <g class="slogan">
      <text class="slogan-lead" x="798" y="126" textLength="89" lengthAdjust="spacingAndGlyphs">don't</text>
      <text class="slogan-main" x="799" y="190" textLength="155" lengthAdjust="spacingAndGlyphs">move</text>
      <text class="slogan-main" x="708" y="270" textLength="322" lengthAdjust="spacingAndGlyphs">re-imagine</text>
    </g>

    <line class="divider" x1="687" y1="342" x2="687" y2="400"/>
    <text class="website" x="710" y="356" textLength="322" lengthAdjust="spacing">WWW.VELMBUILD.COM.AU</text>
  </svg>
</main>
</body>
</html>
```